Stationary package for Interior and construction company
Velvet Arch Studios
Professional
Peter Hallsey
Project Manager
Warehouse K42, Dubai Logistics Park Dubai,UAE PO Box 316052
velvetarchdxb@examplemail.test
www.velvetarchdubai.example
We require two business cards with different peoples names. #1 been Peter Hallsey the second persons details are. Simon Ravenholt, Project Manager, Warehouse K42, Dubai Logistics Park, Dubai, UAE, PO Box 316052, Cell- +971 50 6185072 Ph- +971 4 3061825 Email - s.ravenholt@velvetarchstudios.example Web - www.velvetarchstudios.example Brief, Velvet Arch Studios (VAS) is a luxury fit out and renovations company based in Dubai, UAE. VAS’s clientele are high net worth individuals. The company is looking for a suite of stationary to support their everyday business needs; this should include: • Letterheads (page 1 and page2) • Business cards (Two people) • Envelopes (A4, DL) • Notepad (A4, A5) The company would like to evoke a premium brand through chic, clean and sophisticated stationary items. Colour should not be over-used unnecessarily and the typeface should be clear to read. All artwork provided should be re-writable.
Please just use the logo, add the website to the bottom footer. open to options on layout and design.

```html
<!DOCTYPE html>
<html lang="en">
<head>
<meta charset="utf-8">
<title>Velvet Arch Studios – Business Cards</title>
<link rel="stylesheet" href="https://fonts.googleapis.com/css2?family=Montserrat:wght@700&family=Open+Sans:wght@400;600;700&display=swap">
<style>
  :root {
    --bg: #e9e6e2;
    --card-white: #ffffff;
    --card-grey: #eceded;
    --brand-blue: #1c8bd1;
    --brand-blue-deep: #137bbd;
    --swoosh-grey: #b9bcbf;
    --text-dark: #3a3d40;
    --text-mid: #5d6166;
  }
  * { box-sizing: border-box; margin: 0; padding: 0; }
  html, body { width: 1200px; height: 912px; overflow: hidden; }
  body {
    background: var(--bg);
    position: relative;
    font-family: "Open Sans", Arial, sans-serif;
  }
  .card {
    position: absolute;
    width: 620px;
    height: 354px;
    border-radius: 22px;
    overflow: hidden;
    box-shadow: 0 14px 30px rgba(0,0,0,0.18);
  }
  .card-back {
    left: 90px; top: 90px;
    background: radial-gradient(ellipse at 50% 40%, var(--card-white) 0%, var(--card-grey) 100%);
    display: flex; align-items: center; justify-content: center;
  }
  .card-front {
    left: 490px; top: 468px;
    background: var(--card-white);
  }
  .card-art { position: absolute; inset: 0; }
  .wordmark {
    display: flex; align-items: center; gap: 12px;
    font-family: "Montserrat", Arial, sans-serif;
    font-weight: 700;
    color: var(--brand-blue);
    letter-spacing: 0.04em;
    white-space: nowrap;
  }
  .wordmark-dot {
    border-radius: 50%;
    background: var(--brand-blue);
    flex: none;
  }
  .card-back .wordmark { font-size: 30px; }
  .card-back .wordmark-dot { width: 34px; height: 34px; }
  .card-front .wordmark {
    position: absolute; right: 34px; top: 66px;
    font-size: 19px; gap: 9px;
  }
  .card-front .wordmark-dot { width: 22px; height: 22px; }
  .contact {
    position: absolute; left: 34px; top: 146px;
    color: var(--text-mid);
    font-size: 12px; line-height: 1.55;
  }
  .contact-name { color: var(--brand-blue); font-weight: 700; font-size: 17px; line-height: 1.3; }
  .contact-role { color: var(--text-dark); font-size: 13.5px; margin-bottom: 7px; }
  .contact-address { margin-bottom: 3px; max-width: 250px; }
  .contact-row { display: flex; align-items: center; gap: 7px; }
  .contact-row svg { width: 11px; height: 11px; flex: none; fill: var(--text-mid); }
</style>
</head>
<body>

<section class="card card-back" aria-label="Business card back">
  <div class="wordmark"><span class="wordmark-dot"></span>VELVET ARCH STUDIOS</div>
</section>

<section class="card card-front" aria-label="Business card front">
  <svg class="card-art" viewBox="0 0 620 354" preserveAspectRatio="none" aria-hidden="true">
    <path d="M0 354 L0 318 C 210 345, 430 318, 620 168 L620 354 Z" fill="var(--brand-blue)"/>
    <path d="M0 354 L0 336 C 230 360, 470 325, 620 210 L620 354 Z" fill="var(--brand-blue-deep)" opacity="0.5"/>
    <path d="M250 300 C 420 285, 540 230, 620 130" fill="none" stroke="var(--swoosh-grey)" stroke-width="7" stroke-linecap="round"/>
  </svg>

  <div class="wordmark"><span class="wordmark-dot"></span>VELVET ARCH STUDIOS</div>

  <div class="contact">
    <div class="contact-name">Peter Hallsey</div>
    <div class="contact-role">Project Manager</div>
    <div class="contact-address">Warehouse K42, Dubai Logistics Park<br>Dubai, UAE, PO Box 316052</div>
    <div class="contact-row">
      <svg viewBox="0 0 24 24"><path d="M6.6 10.8a15 15 0 0 0 6.6 6.6l2.2-2.2a1 1 0 0 1 1-.25 11.4 11.4 0 0 0 3.6.57 1 1 0 0 1 1 1V20a1 1 0 0 1-1 1A17 17 0 0 1 3 4a1 1 0 0 1 1-1h3.5a1 1 0 0 1 1 1c0 1.25.2 2.45.57 3.6a1 1 0 0 1-.25 1z"/></svg>
      +971 4 3061825
    </div>
    <div class="contact-row">
      <svg viewBox="0 0 24 24"><path d="M7 1h10a2 2 0 0 1 2 2v18a2 2 0 0 1-2 2H7a2 2 0 0 1-2-2V3a2 2 0 0 1 2-2zm0 3v14h10V4zm5 15.5a1.2 1.2 0 1 0 0 2.4 1.2 1.2 0 0 0 0-2.4z"/></svg>
      +971 50 6185072
    </div>
    <div class="contact-row">
      <svg viewBox="0 0 24 24"><path d="M2 5h20v14H2zm2 2v.5l8 5 8-5V7zm0 2.8V17h16V9.8l-8 5z"/></svg>
      velvetarchdxb@examplemail.test
    </div>
    <div class="contact-row">
      <svg viewBox="0 0 24 24"><path d="M12 2a10 10 0 1 0 0 20 10 10 0 0 0 0-20zm6.9 6h-2.9a15 15 0 0 0-1.3-3.9A8 8 0 0 1 18.9 8zM12 4c.8 1.2 1.5 2.5 1.9 4h-3.8c.4-1.5 1.1-2.8 1.9-4zM4.3 14a8 8 0 0 1 0-4h3.4a16 16 0 0 0 0 4zm.8 2h2.9a15 15 0 0 0 1.3 3.9A8 8 0 0 1 5.1 16zM8 8H5.1a8 8 0 0 1 4.2-3.9A15 15 0 0 0 8 8zm4 12c-.8-1.2-1.5-2.5-1.9-4h3.8c-.4 1.5-1.1 2.8-1.9 4zm2.3-6H9.7a14 14 0 0 1 0-4h4.6a14 14 0 0 1 0 4zm.4 5.9A15 15 0 0 0 16 16h2.9a8 8 0 0 1-4.2 3.9zm1.6-5.9a16 16 0 0 0 0-4h3.4a8 8 0 0 1 0 4z"/></svg>
      www.velvetarchdubai.example
    </div>
  </div>
</section>

</body>
</html>
```